bryn calvo website design

An IT support and IT Security Company - just use dummy text for now for the design. Examples of sites we like the looks and feel of but need it more professional feel are like: www.quorvatech.uk.com , www.halvion.co.uk, www.truvexa.com/professional/, www.zul.com, www.mivlen.com,

Best to message me if you have any questions

Target Market(s)

small to medium UK based companies that require IT support services

Industry/Entity Type

It Company

Contact Information for Business Card

use dummy name, telephone and email for now, will provide details later.

Logo Text

bryn calvo (and then below the logo it should say "your IT, networks and security partner")

Coding

Coded - Design and coding required

Number of Pages Required

5+ page

Colors

Designer to choose colors to be used in the design.

Requirements
Must have
• must be professional, yet simple and clear that this is a serious IT support and IT security company.
Nice to have
• 1)The website homepage must have professional quality pictures of IT support or London city skyline or any picture that projects friendly business partners, professionalism and ready to serve.
• 2) Home page needs to include tabs for following pages 'Services' , 'About Us' , 'Contact Us' 'Home'
• 3) Website built customised using wordpress is ideal and easy for us to manage.
• more room for boxed options from homepage (with pic or image in background)
Should not have
• no checkout trolleys or payment options.

```html
<!DOCTYPE html>
<html lang="en">
<head>
<meta charset="utf-8">
<title>Bryn Calvo – IT Support &amp; Security</title>
<link href="https://fonts.googleapis.com/css2?family=Inter:wght@300;400;500;600;700&family=Kalam:wght@300;400&display=swap" rel="stylesheet">
<style>
:root{
  --red:#e03c25;
  --red-soft:#e8584a;
  --ink:#1e1e1e;
  --text:#555;
  --muted:#888;
  --band:#f4f4f6;
  --white:#fff;
  --line:#e6e6e6;
}
*{box-sizing:border-box;margin:0;padding:0}
html,body{width:1200px;height:2899px;overflow:hidden}
body{font-family:"Inter",Arial,sans-serif;color:var(--text);background:var(--white);position:relative}
section,header,footer{position:relative;width:1200px}

/* header */
.site-header{height:70px;border-top:5px solid var(--red);background:var(--white)}
.brand{position:absolute;left:56px;top:17px;font-size:28px;font-weight:700;color:var(--red);letter-spacing:-.5px}
.main-nav{position:absolute;left:446px;top:24px;display:flex;gap:38px;font-size:14px;color:var(--ink);font-weight:500}
.chat-link{position:absolute;left:934px;top:22px;font-size:14px;color:var(--ink);display:flex;align-items:center;gap:5px}
.call-btn{position:absolute;left:1000px;top:16px;width:162px;height:34px;border-radius:17px;background:var(--red-soft);color:var(--white);font-size:13px;font-weight:600;display:flex;align-items:center;justify-content:center}

/* hero */
.hero{height:545px;background:linear-gradient(180deg,#5d6a7d 0%,#7b8593 40%,#4d5560 75%,#3b3f45 100%);text-align:center;color:var(--white)}
.hero-title{position:absolute;top:176px;width:100%;font-family:"Kalam",cursive;font-weight:300;font-size:40px;letter-spacing:.5px}
.hero-sub{position:absolute;top:250px;width:100%;font-size:19px;font-weight:300;line-height:31px}
.hero-btn{position:absolute;left:481px;top:352px;width:240px;height:40px;border:2px solid var(--white);border-radius:6px;font-size:14px;font-weight:600;display:flex;align-items:center;justify-content:center}

/* features */
.features{height:303px;background:var(--band)}
.feature{position:absolute;top:60px;width:360px;text-align:center}
.feature svg{display:block;margin:0 auto;height:80px}
.feature h3{margin-top:32px;font-size:18px;color:var(--ink);font-weight:600}
.feature p{margin:18px auto 0;width:300px;font-size:13px;line-height:21px;color:var(--text)}
.feature-rule{position:absolute;top:95px;height:2px;width:150px;background:var(--red-soft)}

/* section headings */
.section-title{position:absolute;top:20px;width:100%;text-align:center;font-size:22px;font-weight:600;color:var(--ink)}
.section-title em{font-style:normal;color:var(--red)}
.dotted-rule{position:absolute;top:58px;left:52px;width:1096px;border-top:2px dotted var(--red-soft)}

/* solutions */
.solutions{height:468px}
.solution{position:absolute;top:124px;width:280px;text-align:center}
.solution-photo{width:178px;height:178px;border-radius:50%;margin:0 auto}
.solution h3{margin-top:30px;font-size:18px;color:var(--ink);font-weight:600}
.solution p{margin:18px auto 0;width:250px;font-size:13px;line-height:20px}
.tone-blue{background:radial-gradient(circle,#2f8fb0,#0d4f72)}
.tone-gold{background:radial-gradient(circle,#c9a514,#7d6508)}
.tone-teal{background:radial-gradient(circle,#1c8d8f,#0b4d55)}
.tone-amber{background:radial-gradient(circle,#f0a020,#c26b08)}

/* protect */
.protect{height:426px;display:flex}
.protect-copy{width:600px;height:100%;background:var(--red);color:var(--white);padding:58px 50px 0}
.protect-copy h2{font-size:40px;font-weight:700;letter-spacing:-.3px}
.protect-copy p{margin-top:18px;font-size:13.5px;font-weight:500;line-height:20px}
.protect-copy p+p{margin-top:16px}
.outline-btn{display:inline-flex;margin-top:30px;width:132px;height:38px;border:2px solid var(--white);border-radius:19px;align-items:center;justify-content:center;font-size:13px;font-weight:600}
.protect-photo{width:600px;height:100%;background:linear-gradient(120deg,#c9d0dc 0%,#8f9bb0 45%,#5b6780 100%)}

/* testimonials */
.testimonials{height:409px;background:var(--band)}
.quote{position:absolute;width:540px}
.quote p{font-size:12.5px;font-style:italic;line-height:19px;color:var(--muted)}
.quote cite{display:block;margin-top:12px;font-style:normal;font-size:13px;color:var(--ink);font-weight:500}
.quote.left{text-align:right}
.avatar{position:absolute;width:78px;height:78px;border-radius:50%;background:radial-gradient(circle,#d6c7bb,#a08b7c);border:4px solid #e9e9ec}
.quote-grid-v{position:absolute;left:600px;top:95px;height:280px;border-left:2px dotted var(--red-soft)}
.quote-grid-h{position:absolute;left:52px;top:238px;width:1096px;border-top:2px dotted var(--red-soft)}

/* customers */
.customers{height:233px}
.client{position:absolute;top:98px;width:120px;text-align:center}
.client-mark{display:flex;align-items:center;justify-content:center;gap:6px;height:36px;font-size:12px;font-weight:600;color:var(--ink)}
.client-mark i{display:inline-block;width:12px;height:12px;border-radius:50%;background:var(--c)}
.client span{display:block;margin-top:14px;font-size:13px;letter-spacing:1px;color:#666}

/* footer */
.site-footer{height:444px;border-top:3px solid var(--red)}
.col-title{font-size:18px;font-weight:600;color:var(--ink)}
.mail-form{position:absolute;left:52px;top:38px;width:254px}
.field{border:1px solid #bbb;border-radius:4px;height:32px;font-size:12px;color:#888;padding:9px 12px}
.field-row{display:flex;gap:18px;margin-top:24px}
.field-row .field{width:118px}
.mail-form .field.full{margin-top:18px}
.mail-form .field.message{height:70px}
.send-btn{margin-top:20px;width:142px;height:32px;border-radius:16px;background:var(--red);color:var(--white);font-size:13px;font-weight:600;display:flex;align-items:center;justify-content:center}
.hq{position:absolute;left:334px;top:44px;width:532px;text-align:center}
.map{margin-top:24px;height:224px;background:linear-gradient(135deg,#cfe3f2 0%,#e9eef1 45%,#9fc7e8 100%);border-radius:2px}
.contact{position:absolute;left:896px;top:38px;width:260px;font-size:13px;line-height:20px;color:var(--ink)}
.contact p{margin-top:14px}
.socials{display:flex;gap:10px;margin-top:20px}
.socials i{width:28px;height:28px;border-radius:50%;background:var(--red)}
.copyright{position:absolute;left:52px;top:369px;width:1096px;border-top:1px solid #d8d8d8;text-align:center;padding-top:24px;font-size:13px;color:var(--ink)}
.bottom-bar{position:absolute;left:0;bottom:0;width:1200px;height:5px;background:var(--red)}
</style>
</head>
<body>

<header class="site-header">
  <div class="brand">BRYN CALVO</div>
  <nav class="main-nav"><span>ABOUT US</span><span>OUR SERVICE</span><span>CONTACT US</span></nav>
  <div class="chat-link">Chat
    <svg width="14" height="13" viewBox="0 0 14 13" fill="none" stroke="#1e1e1e" stroke-width="1.3"><path d="M2 1h10a1 1 0 0 1 1 1v6a1 1 0 0 1-1 1H6l-3 3V9H2a1 1 0 0 1-1-1V2a1 1 0 0 1 1-1z"/></svg>
  </div>
  <div class="call-btn">Call: +44 (500) 61 72 83</div>
</header>

<section class="hero" role="img" aria-label="City skyline with office towers under a cloudy sky">
  <h1 class="hero-title">When IT matters to you, IT matters to us.</h1>
  <p class="hero-sub">Accelerate your business growth and boost efficiency from day one<br>with fast and effective 24/7 IT support and technology solutions</p>
  <div class="hero-btn">View our IT Support Solutions</div>
</section>

<section class="features">
  <div class="feature" style="left:46px">
    <svg viewBox="0 0 80 80" width="80" fill="none" stroke="#e8584a" stroke-width="1.6"><path d="M40 8 L68 18 V40 C68 58 54 68 40 74 C26 68 12 58 12 40 V18 Z"/><path d="M27 48 a8 8 0 0 1 3-15 a11 11 0 0 1 21 2 a7 7 0 0 1 0 13 Z"/></svg>
    <h3>24/7 IT support</h3>
    <p>Our experts provide IT support 24/7, 365 days a year</p>
  </div>
  <div class="feature-rule" style="left:338px"></div>
  <div class="feature" style="left:420px">
    <svg viewBox="0 0 80 80" width="80" fill="none" stroke="#e8584a" stroke-width="1.8"><path d="M22 4v72M40 4v72M58 4v72"/><circle cx="22" cy="24" r="6" fill="#fff"/><circle cx="40" cy="50" r="6" fill="#fff"/><circle cx="58" cy="32" r="6" fill="#fff"/></svg>
    <h3>Super fast service</h3>
    <p>Our engineers resolve your IT issues within just 10 minutes</p>
  </div>
  <div class="feature-rule" style="left:712px"></div>
  <div class="feature" style="left:794px">
    <svg viewBox="0 0 80 80" width="80" fill="none" stroke="#e8584a" stroke-width="1.8"><path d="M64 40a24 24 0 1 1-8-18"/><path d="M56 10v12h12"/><path d="M52 40a12 12 0 1 1-4-9"/></svg>
    <h3>IT expertise</h3>
    <p>Our team are trained and certified to provide reliable, expert IT support</p>
  </div>
</section>

<section class="solutions">
  <h2 class="section-title">A solution for <em>Your business</em></h2>
  <div class="dotted-rule"></div>
  <div class="solution" style="left:39px">
    <div class="solution-photo tone-blue" role="img" aria-label="Blue-toned office scene with a building icon"></div>
    <h3>Every Business Size</h3>
    <p>Solutions for large, midsized and small, fast-growing businesses.</p>
  </div>
  <div class="solution" style="left:319px">
    <div class="solution-photo tone-gold" role="img" aria-label="Gold-toned workplace scene with a factory icon"></div>
    <h3>Every Industry</h3>
    <p>Industry-specific functionality spanning a broad range of businesses.</p>
  </div>
  <div class="solution" style="left:600px">
    <div class="solution-photo tone-teal" role="img" aria-label="Teal-toned meeting scene with a team icon"></div>
    <h3>Every Role</h3>
    <p>Solutions addressing the needs of the CEO, CFO, Controller and CIO.</p>
  </div>
  <div class="solution" style="left:880px">
    <div class="solution-photo tone-amber" role="img" aria-label="Amber-toned desk scene with a shuffle icon"></div>
    <h3>Current Software</h3>
    <p>Replacing legacy accounting, ERP and other business systems.</p>
  </div>
</section>

<section class="protect">
  <div class="protect-copy">
    <h2>Protecting your Business</h2>
    <p>Sed ut perspiciatis unde omnis iste natus error sit voluptatem accusantium doloremque laudantium, totam rem aperiam, eaque ipsa quae ab illo inventore veritatis et quasi architecto beatae vitae dicta sunt explicabo. Nemo enim ipsam voluptatem quia voluptas.</p>
    <p>Sed ut perspiciatis unde omnis iste natus error sit voluptatem accusantium doloremque laudantium, totam rem aperiam, eaque ipsa quae ab illo inventore veritatis et quasi architecto beatae vitae dicta sunt explicabo</p>
    <div class="outline-btn">LEARN MORE</div>
  </div>
  <div class="protect-photo" role="img" aria-label="Business meeting in a bright glass-walled office"></div>
</section>

<section class="testimonials">
  <h2 class="section-title">What <em>People Say</em></h2>
  <div class="dotted-rule"></div>
  <div class="quote-grid-v"></div>
  <div class="quote-grid-h"></div>

  <div class="quote left" style="left:0;top:117px;width:462px">
    <p>Duis aute irure dolor in reprehenderit in voluptate velit esse cillum dolore eu fugiat nulla pariatur. Excepteur sint occaecat cupidatat non proident, sunt in culpa qui officia deserunt mollit.</p>
    <cite>Dave Cohen, Operations Manager</cite>
  </div>
  <div class="avatar" style="left:488px;top:114px" role="img" aria-label="Portrait of a client"></div>

  <div class="avatar" style="left:632px;top:114px" role="img" aria-label="Portrait of a client"></div>
  <div class="quote" style="left:738px;top:117px;width:410px">
    <p>Provident, similique sunt in culpa qui officia deserunt mollitia animi, id est laborum et dolorum fuga. Et harum quidem rerum facilis est et expedita distinctio. Nam libero tempore, cum soluta nobis.</p>
    <cite>Linda Grey, Creative Designer</cite>
  </div>

  <div class="quote left" style="left:0;top:256px;width:462px">
    <p>Luis aute irure dolor in reprehenderit in pluptate velit esse cillum dolore eu fugiat nulla pariatur. Excepteur sint occaecat cupidatat non proident, sunt in culpa qui officia deserunt mollit.</p>
    <cite>Martha Lee, Manager</cite>
  </div>
  <div class="avatar" style="left:488px;top:253px" role="img" aria-label="Portrait of a client"></div>

  <div class="avatar" style="left:632px;top:253px" role="img" aria-label="Portrait of a client"></div>
  <div class="quote" style="left:738px;top:256px;width:410px">
    <p>At vero eos et accusamus et iusto odio dignissimos ducimus qui blanditiis praesentium voluptatum deleniti atque corrupti quos dolores et quas molestias excepturi sint occaecati asperiores.</p>
    <cite>Tom Lardy, Developer</cite>
  </div>
</section>

<section class="customers">
  <h2 class="section-title">Our <em>Customers</em></h2>
  <div class="dotted-rule"></div>
  <div class="client" style="left:138px"><div class="client-mark"><i style="--c:#3aa53a"></i>Veltrane</div><span>VELTRANE</span></div>
  <div class="client" style="left:275px"><div class="client-mark"><i style="--c:#1f6fb6"></i>Ostra</div><span>OSTRA</span></div>
  <div class="client" style="left:411px"><div class="client-mark"><i style="--c:#c8102e"></i>Corvale</div><span>CORVALE</span></div>
  <div class="client" style="left:547px"><div class="client-mark"><i style="--c:#3b73b9"></i>Lorem</div><span>LOREM</span></div>
  <div class="client" style="left:682px"><div class="client-mark"><i style="--c:#1d3f8b"></i>Brightwell</div><span>BRIGHTWELL POWER</span></div>
  <div class="client" style="left:820px"><div class="client-mark"><i style="--c:#444"></i>Nerolink</div><span>NEROLINK</span></div>
  <div class="client" style="left:955px"><div class="client-mark"><i style="--c:#f29111"></i>Talvenor</div><span>TALVENOR</span></div>
</section>

<footer class="site-footer">
  <div class="mail-form">
    <h3 class="col-title">Feel Free to Mail</h3>
    <div class="field-row"><div class="field">Name *</div><div class="field">Email *</div></div>
    <div class="field full">Subject</div>
    <div class="field full message">Write Your Message Here...</div>
    <div class="send-btn">SEND MESSAGE</div>
  </div>
  <div class="hq">
    <h3 class="col-title">Headquarters</h3>
    <div class="map" role="img" aria-label="Street map of the headquarters location by the harbour"></div>
  </div>
  <div class="contact">
    <h3 class="col-title">Contact Info</h3>
    <p>Our staff is available to you from 9AM until 5PM on weekdays.</p>
    <p>Phone: +1 (500) 418 23 56</p>
    <p>Office: Your Company Address</p>
    <p>Email: info@yourdomain.com</p>
    <h3 class="col-title" style="margin-top:16px">Follow Us on</h3>
    <div class="socials"><i></i><i></i><i></i><i></i><i></i></div>
  </div>
  <div class="copyright">© 2006 - 2018. All Rights Reserved by Bryn Calvo</div>
  <div class="bottom-bar"></div>
</footer>

</body>
</html>
```